Bref créative
Stationery for HR Consultancy
Business card, letterhead & compliment slip
Use same font as used in my logo
Century Gothic
Professional
Rosalind Ashcombe, FMPSB
Managing Consultant
Cambridgeshire
United Kingdom
rashcombe@VelmoreCS.example
www.VelmoreCS.example
Coloured logo on business card front. open to your suggestions for other stationery.
the purple is the primary brand colour. Green is the accent colour.
the logo colour variations that are available and colour/font descriptions are attached.
i'll provide feedback to help steer the designs if needed.
Logo with text on the card reverse. I would consider a white on purple/green background (brand colours) on the reverse, as well as the coloured logo on white background.
White background on the front of card.
letterhead text positions

```html
<!DOCTYPE html>
<html lang="en">
<head>
<meta charset="utf-8">
<title>VelmoreCS Stationery</title>
<link rel="stylesheet" href="https://fonts.googleapis.com/css2?family=Questrial&display=swap">
<style>
  :root {
    --purple: #5e1b72;
    --purple-light: #8a3aa0;
    --green: #79b446;
    --paper: #ffffff;
    --ground: #ececec;
    --ink: #555555;
    --faint: #efe9f1;
  }
  * { margin: 0; padding: 0; box-sizing: border-box; }
  html, body { width: 1200px; height: 936px; overflow: hidden; background: var(--ground); }
  body { position: relative; font-family: "Questrial", "Century Gothic", sans-serif; color: var(--ink); }
  .sheet { position: absolute; background: var(--paper); overflow: hidden; box-shadow: 0 2px 6px rgba(0,0,0,.12); }
  .swoosh { position: absolute; left: 0; top: 0; width: 100%; }
  .brand { position: absolute; display: flex; align-items: center; gap: 8px; white-space: nowrap; }
  .brand-dot { border-radius: 50%; background: var(--purple); flex: none; }
  .brand-name { color: var(--purple); line-height: 1; }
  .tagline { position: absolute; line-height: 1.3; white-space: nowrap; }

  .letterhead { left: 185px; top: 36px; width: 420px; height: 574px; }
  .letterhead .brand { left: 26px; top: 50px; }
  .letterhead .brand-dot { width: 14px; height: 14px; }
  .letterhead .brand-name { font-size: 18px; }
  .letterhead .tagline { left: 48px; top: 72px; font-size: 7px; color: var(--purple); }
  .watermark { position: absolute; left: 0; right: 0; top: 270px; text-align: center; font-size: 44px; color: var(--faint); }
  .contact { position: absolute; left: 26px; bottom: 36px; list-style: none; font-size: 6.5px; line-height: 10px; white-space: nowrap; }
  .contact li::before { content: ""; display: inline-block; width: 4px; height: 4px; border-radius: 50%; background: var(--purple); margin-right: 5px; vertical-align: middle; }

  .folder { left: 635px; top: 36px; width: 465px; height: 581px; }
  .folder .brand { left: 70px; top: 262px; gap: 14px; }
  .folder .brand-dot { width: 44px; height: 44px; }
  .folder .brand-name { font-size: 42px; }
  .folder .tagline { left: 128px; top: 312px; font-size: 15px; color: var(--purple); }
  .folder .tagline .sub { color: var(--green); display: block; padding-left: 48px; }

  .card-front { left: 40px; top: 655px; width: 184px; height: 107px; }
  .card-front .brand { left: 10px; top: 16px; gap: 5px; }
  .card-front .brand-dot { width: 10px; height: 10px; }
  .card-front .brand-name { font-size: 13px; }
  .card-front .tagline { left: 10px; top: 33px; font-size: 5px; color: var(--purple); }
  .card-front .contact { left: 10px; bottom: 10px; font-size: 4.5px; line-height: 7px; }
  .card-front .contact li::before { width: 3px; height: 3px; margin-right: 3px; }

  .card-back { left: 40px; top: 780px; width: 184px; height: 107px; background: linear-gradient(120deg, var(--purple-light), var(--purple)); }
  .card-back .brand { left: 0; right: 0; top: 38px; justify-content: center; }
  .card-back .brand-name { color: var(--paper); font-size: 20px; }
  .card-back .web { position: absolute; left: 10px; bottom: 8px; font-size: 5px; color: var(--paper); opacity: .8; }

  .slip { left: 264px; top: 668px; width: 434px; height: 214px; }
  .slip .brand { left: 22px; top: 44px; gap: 6px; }
  .slip .brand-dot { width: 12px; height: 12px; }
  .slip .brand-name { font-size: 17px; }
  .slip .tagline { left: 22px; top: 66px; font-size: 6px; color: var(--purple); }
  .slip .contact { left: 22px; top: 84px; bottom: auto; font-size: 5px; line-height: 8px; }
  .slip .contact li::before { display: none; }

  .envelope { left: 737px; top: 668px; width: 431px; height: 214px; }
  .envelope .web { position: absolute; left: 0; right: 0; top: 32px; text-align: center; font-size: 12px; letter-spacing: 3px; color: var(--paper); }
</style>
</head>
<body>

<section class="sheet letterhead">
  <svg class="swoosh" viewBox="0 0 100 20" height="100" preserveAspectRatio="none" aria-hidden="true">
    <path d="M0 0 H100 V15 C70 5 35 2 0 3 Z" fill="var(--purple)"/>
    <path d="M0 4.5 C35 3.5 70 7 100 17" fill="none" stroke="var(--green)" stroke-width="1.2" vector-effect="non-scaling-stroke"/>
  </svg>
  <div class="brand"><span class="brand-dot"></span><span class="brand-name">VelmoreCS</span></div>
  <p class="tagline">aligning people with purpose</p>
  <p class="watermark">VelmoreCS</p>
  <ul class="contact">
    <li>Rosalind Ashcombe, FMPSB</li>
    <li>Managing Consultant</li>
    <li>East of England Office</li>
    <li>rashcombe@VelmoreCS.example</li>
    <li>www.VelmoreCS.example</li>
  </ul>
</section>

<section class="sheet folder">
  <svg class="swoosh" viewBox="0 0 100 20" height="110" preserveAspectRatio="none" aria-hidden="true">
    <path d="M0 0 H100 V17 C70 5 35 1 0 2 Z" fill="var(--purple)"/>
    <path d="M0 3.2 C35 2.5 70 6.5 100 19" fill="none" stroke="var(--green)" stroke-width="2" vector-effect="non-scaling-stroke"/>
  </svg>
  <div class="brand"><span class="brand-dot"></span><span class="brand-name">VelmoreCS</span></div>
  <p class="tagline">Workforce Advisory Partners<span class="sub">aligning people with purpose</span></p>
</section>

<section class="sheet card-front">
  <svg class="swoosh" viewBox="0 0 100 20" height="34" preserveAspectRatio="none" aria-hidden="true">
    <path d="M0 0 H100 V16 C70 5 35 1 0 2 Z" fill="var(--purple)"/>
    <path d="M0 3.5 C35 2.5 70 6.5 100 18.5" fill="none" stroke="var(--green)" stroke-width="1" vector-effect="non-scaling-stroke"/>
  </svg>
  <div class="brand"><span class="brand-dot"></span><span class="brand-name">VelmoreCS</span></div>
  <p class="tagline">aligning people with purpose</p>
  <ul class="contact">
    <li>Rosalind Ashcombe, FMPSB</li>
    <li>rashcombe@VelmoreCS.example</li>
    <li>www.VelmoreCS.example</li>
  </ul>
</section>

<section class="sheet card-back">
  <div class="brand"><span class="brand-name">VelmoreCS</span></div>
  <p class="web">www.VelmoreCS.example</p>
</section>

<section class="sheet slip">
  <svg class="swoosh" viewBox="0 0 100 20" height="42" preserveAspectRatio="none" aria-hidden="true">
    <path d="M0 0 H100 V16 C70 5 35 1 0 2 Z" fill="var(--purple)"/>
    <path d="M0 3.5 C35 2.5 70 6.5 100 18.5" fill="none" stroke="var(--green)" stroke-width="1.2" vector-effect="non-scaling-stroke"/>
  </svg>
  <div class="brand"><span class="brand-dot"></span><span class="brand-name">VelmoreCS</span></div>
  <p class="tagline">aligning people with purpose</p>
  <ul class="contact">
    <li>With compliments</li>
    <li>www.VelmoreCS.example</li>
  </ul>
</section>

<section class="sheet envelope">
  <svg class="swoosh" viewBox="0 0 100 20" height="78" preserveAspectRatio="none" aria-hidden="true">
    <defs>
      <linearGradient id="flap" x1="0" x2="1">
        <stop offset="0" stop-color="var(--purple-light)"/>
        <stop offset="1" stop-color="var(--purple)"/>
      </linearGradient>
    </defs>
    <path d="M0 0 H100 V20 C70 13 35 10 0 12 Z" fill="url(#flap)"/>
  </svg>
  <p class="web">WWW.VELMORECS.EXAMPLE</p>
</section>

</body>
</html>
```